Mine Engineering Consultancy specializing in
* Pit optimization
* Mine Design
* Scheduling
* Mine Rehabilitation

Mining

RVT Mining Pty Ltd
Dennis Holloway
Director/Principle Mining Engineer
Mobile 0418263591
Email dennis.holloway@rvtmining-example.com

```html
<!DOCTYPE html>
<html lang="en">
<head>
<meta charset="utf-8">
<title>RVT Mining Pty Ltd – Business Card</title>
<link href="https://fonts.googleapis.com/css2?family=Open+Sans:wght@400;600;700&display=swap" rel="stylesheet">
<style>
  :root {
    --page-bg: #e9eaec;
    --card-bg: #ffffff;
    --brand-blue: #1b6fba;
    --brand-blue-light: #8ea8dc;
    --ink: #1a1a1a;
    --card-shadow: rgba(0, 0, 0, 0.18);
  }
  * { box-sizing: border-box; margin: 0; padding: 0; }
  html, body {
    width: 1200px;
    height: 864px;
    overflow: hidden;
    background: var(--page-bg);
    font-family: "Open Sans", Arial, sans-serif;
  }
  .canvas {
    position: relative;
    width: 1200px;
    height: 864px;
  }
  .card {
    position: absolute;
    width: 580px;
    height: 332px;
    background: var(--card-bg);
    box-shadow: 0 6px 18px var(--card-shadow);
  }
  /* Front face */
  .card--front { left: 330px; top: 64px; }
  .front-wordmark {
    position: absolute;
    left: 0; right: 0; top: 70px;
    text-align: center;
    color: var(--brand-blue);
    font-weight: 700;
  }
  .front-wordmark__name {
    display: block;
    font-size: 104px;
    line-height: 1;
    letter-spacing: 6px;
  }
  .front-wordmark__entity {
    display: block;
    margin-top: 18px;
    font-size: 31px;
    letter-spacing: 2px;
  }
  /* Back face */
  .card--back { left: 190px; top: 468px; }
  .back-wordmark {
    position: absolute;
    left: 44px; top: 30px;
    color: var(--brand-blue);
    font-weight: 700;
    font-size: 74px;
    line-height: 1;
    letter-spacing: 4px;
  }
  .contact-name {
    position: absolute;
    left: 44px; top: 148px;
    color: var(--brand-blue);
    font-weight: 700;
    font-size: 19px;
  }
  .contact-title {
    position: absolute;
    left: 44px; top: 178px;
    color: var(--ink);
    font-size: 14px;
  }
  .contact-list {
    position: absolute;
    left: 44px; top: 232px;
    list-style: none;
  }
  .contact-list__item {
    display: flex;
    align-items: center;
    gap: 12px;
    height: 24px;
    margin-bottom: 4px;
    color: var(--ink);
    font-size: 14px;
  }
  .contact-icon {
    width: 18px;
    height: 16px;
    flex: none;
  }
  .side-entity {
    position: absolute;
    right: 34px; top: 50%;
    transform: translate(50%, -50%) rotate(-90deg);
    transform-origin: center;
    white-space: nowrap;
    color: var(--brand-blue-light);
    font-weight: 700;
    font-size: 29px;
    letter-spacing: 1px;
    margin-right: 18px;
  }
</style>
</head>
<body>
<main class="canvas">
  <section class="card card--front" aria-label="Card front">
    <h1 class="front-wordmark">
      <span class="front-wordmark__name">RVT</span>
      <span class="front-wordmark__entity">MINING PTY LTD</span>
    </h1>
  </section>

  <section class="card card--back" aria-label="Card back">
    <div class="back-wordmark">RVT</div>
    <h2 class="contact-name">Dennis Holloway</h2>
    <p class="contact-title">Director/Principle Mining Engineer</p>
    <ul class="contact-list">
      <li class="contact-list__item">
        <svg class="contact-icon" viewBox="0 0 18 16" aria-hidden="true">
          <rect width="18" height="16" fill="var(--brand-blue)"/>
          <path d="M5 5.5c0-1 1.5-1.6 4-1.6s4 .6 4 1.6v1h-2V5.8H7v.7H5z" fill="#fff"/>
          <rect x="5.5" y="8" width="7" height="4" rx="0.6" fill="#fff"/>
        </svg>
        <span>0418263591</span>
      </li>
      <li class="contact-list__item">
        <svg class="contact-icon" viewBox="0 0 18 16" aria-hidden="true">
          <rect width="18" height="16" fill="var(--brand-blue)"/>
          <rect x="4" y="4.5" width="10" height="7" fill="none" stroke="#fff" stroke-width="1.2"/>
          <path d="M4 4.5l5 4 5-4" fill="none" stroke="#fff" stroke-width="1.2"/>
        </svg>
        <span>dennis.holloway@rvtmining-example.com</span>
      </li>
    </ul>
    <div class="side-entity">MINING PTY LTD</div>
  </section>
</main>
</body>
</html>
```